Private Equity Company Stationary
business card, letterhead, envelope, fax cover
#46 please eliminate the email address from the envelope. Thanks
#34 Birchway Holdings Group Header and remove big logo/watermark from the center of the page.
#33 remove all the phone numbers from envelope
#21 please eliminate border (header and footer) from business card, letterhead, fax coverand just leave it plain. Please re-submit with changes
envelope flaps to remain white
The only place the cell phone number is needed is on the business card.
I need some clarification before I can submit a satifactory design.
1. Do we need to mention the name "Holdings Grouup Advisory, Inc." compulsarily in any of the media.
2. Are there any limitations on the no of colours that can be used as printing costs can vary significantly.

```html
<!DOCTYPE html>
<html lang="en">
<head>
<meta charset="utf-8">
<title>Birchway Holdings Group – Stationery</title>
<link href="https://fonts.googleapis.com/css2?family=Cormorant+Garamond:wght@400;500;600&display=swap" rel="stylesheet">
<style>
  :root{
    --navy:#1f2f5e;
    --taupe:#8a7a62;
    --paper:#ffffff;
    --ink:#3a3a3a;
    --muted:#7a7a7a;
    --ghost:#eceef2;
    --fold:#d6d9e0;
    --stage:#e7e4df;
  }
  *{box-sizing:border-box;margin:0;padding:0}
  html,body{width:1200px;height:785px;overflow:hidden}
  body{background:var(--stage);font-family:"Cormorant Garamond",Georgia,serif;color:var(--ink);position:relative}

  .sheet{position:absolute;background:var(--paper);box-shadow:0 2px 8px rgba(0,0,0,.18);overflow:hidden}
  address{font-style:normal}

  .brand{display:flex;align-items:center;gap:8px;color:var(--navy);font-weight:500;letter-spacing:.08em;text-transform:uppercase;white-space:nowrap}
  .brand__square{width:14px;height:14px;background:var(--navy);flex:none}

  .ghost-square{position:absolute;background:var(--ghost)}

  /* Envelope – back */
  .envelope-back{left:60px;top:20px;width:555px;height:250px}
  .envelope-back__flap{position:absolute;left:0;top:0;width:100%;height:110px}
  .envelope-back .brand--flap{position:absolute;left:50%;top:38px;transform:translateX(-50%);font-size:13px}
  .envelope-back .brand--body{position:absolute;left:50%;top:150px;transform:translateX(-50%);font-size:16px}
  .envelope-back .ghost-square{right:22px;bottom:12px;width:90px;height:90px}

  /* Envelope – front */
  .envelope-front{left:55px;top:405px;width:555px;height:355px}
  .envelope-front__flap{position:absolute;left:0;top:0;width:100%;height:60px;border-bottom:1px solid var(--fold)}
  .envelope-front__edge{position:absolute;left:0;top:60px;width:16px;bottom:0;background:var(--navy)}
  .envelope-front .brand--flap{position:absolute;left:50%;top:21px;transform:translateX(-50%);font-size:14px}
  .envelope-front .brand--body{position:absolute;left:36px;top:92px;font-size:16px}
  .envelope-front .ghost-square{left:250px;bottom:30px;width:95px;height:95px}
  .return-address{position:absolute;left:36px;bottom:26px;font-size:11px;line-height:1.35;color:var(--ink)}

  /* Letterhead */
  .letterhead{left:643px;top:12px;width:535px;height:760px}
  .letterhead > .brand{position:absolute;left:30px;top:28px;font-size:17px}
  .letterhead__address{position:absolute;right:34px;top:24px;text-align:right;font-size:11px;line-height:1.35}
  .letterhead__contact{position:absolute;left:30px;bottom:28px;font-size:10px;line-height:1.4}
  .letterhead__contact b{font-weight:600;display:inline-block;width:34px}
  .letterhead > .ghost-square{right:40px;bottom:60px;width:150px;height:150px}

  /* Business cards */
  .card{position:absolute;background:var(--paper);box-shadow:0 1px 5px rgba(0,0,0,.25);overflow:hidden}
  .card-front{left:58px;top:160px;width:254px;height:150px}
  .card-front__bar-navy{position:absolute;left:0;top:0;width:10px;height:60%;background:var(--navy)}
  .card-front__bar-taupe{position:absolute;left:0;bottom:0;width:10px;height:40%;background:var(--taupe)}
  .card-front .brand{position:absolute;left:20px;top:62px;font-size:10px;gap:5px}
  .card-front .brand__square{width:9px;height:9px}
  .card-front__holder{position:absolute;right:14px;top:14px;text-align:right}
  .card-front__name{font-size:11px;font-weight:600;color:var(--navy)}
  .card-front__title{font-size:8px;color:var(--muted)}
  .card-front__address{position:absolute;right:14px;top:48px;text-align:right;font-size:8px;line-height:1.3}
  .card-front__contact{position:absolute;right:14px;bottom:10px;text-align:right;font-size:8px;line-height:1.3}
  .card-front__contact b{font-weight:600}

  .card-back{left:58px;top:343px;width:254px;height:150px}
  .card-back__mark{position:absolute;left:50%;top:30px;transform:translateX(-50%);width:38px;height:38px;background:var(--navy)}
  .card-back__name{position:absolute;left:0;right:0;top:80px;text-align:center;font-size:10px;color:var(--navy);letter-spacing:.08em;text-transform:uppercase}
  .card-back__web{position:absolute;left:0;right:0;bottom:20px;text-align:center;font-size:9px;letter-spacing:.25em;color:var(--ink)}
</style>
</head>
<body>

<section class="sheet envelope-back" aria-label="Envelope, back">
  <svg class="envelope-back__flap" viewBox="0 0 555 110" preserveAspectRatio="none" aria-hidden="true">
    <polyline points="0,20 235,105 320,105 555,20" fill="none" stroke="#d6d9e0" stroke-width="1.5"/>
  </svg>
  <div class="brand brand--flap"><span class="brand__square"></span>Birchway Holdings Group</div>
  <div class="brand brand--body"><span class="brand__square"></span>Birchway Holdings Group</div>
  <div class="ghost-square"></div>
</section>

<section class="sheet envelope-front" aria-label="Envelope, front">
  <div class="envelope-front__flap"></div>
  <div class="envelope-front__edge"></div>
  <div class="brand brand--flap"><span class="brand__square"></span>Birchway Holdings Group</div>
  <div class="brand brand--body"><span class="brand__square"></span>Birchway Holdings Group</div>
  <div class="ghost-square"></div>
  <address class="return-address">418 W Harlan Ave<br>Suite 1140<br>Fairview, CA 90031</address>
</section>

<section class="sheet letterhead" aria-label="Letterhead">
  <div class="brand"><span class="brand__square"></span>Birchway Holdings Group</div>
  <address class="letterhead__address">418 W Harlan Ave<br>Suite 1140<br>Fairview, CA 90031</address>

  <article class="card card-front" aria-label="Business card, front">
    <div class="card-front__bar-navy"></div>
    <div class="card-front__bar-taupe"></div>
    <div class="brand"><span class="brand__square"></span>Birchway Holdings</div>
    <div class="card-front__holder">
      <div class="card-front__name">Elliot Valmorent</div>
      <div class="card-front__title">Managing Partner</div>
    </div>
    <address class="card-front__address">418 W Harlan Ave<br>Suite 1140<br>Fairview, CA 90031</address>
    <div class="card-front__contact">
      <b>Phone</b> (213) 555-0148<br>
      <b>Cell</b> (213) 555-0172<br>
      <b>Fax</b> (213) 555-0190<br>
      <b>Email</b> ev@birchwayhg.com<br>
      www.birchwayhg.com
    </div>
  </article>

  <article class="card card-back" aria-label="Business card, back">
    <div class="card-back__mark"></div>
    <div class="card-back__name">Birchway Holdings Group</div>
    <div class="card-back__web">www.birchwayhg.com</div>
  </article>

  <div class="ghost-square"></div>

  <div class="letterhead__contact">
    <b>Phone</b> (213) 555-0148<br>
    <b>Fax</b> (213) 555-0190<br>
    <b>Email</b> info@birchwayhg.com<br>
    www.birchwayhg.com
  </div>
</section>

</body>
</html>
```